Verpackungen für Glückskekse
Zielgruppe
Wir sind ein Produzent für regionale Glückskekse aus Niederbayern. Unsere Zielgruppe sind hauptsächlich Frauen zwischen 25 und 55, da unsere Glückskekse hauptsächlich als Gastgeschenke für Hochzeiten, Taufen und Geburtstage verwendet werden.
Aufgabenstellung
Das Vektor Design ist für eine Kartonbox in 12x12x12cm für 12 einzeln verpackte Glückskekse. Auf der Box und auf den Glückskeksen soll der Spruch 'Schön, dass du da bist' stehen.
Primär sollen die Glückskekse auf Hochzeiten eingesetzt werden, die im Boho/Beige-Weiß/Pampasgras Stil dekoriert sind.
Ich habe bereits einen ersten Entwurf, bin mir aber dabei noch nicht ganz sicher. Deshalb sollte der Vorschlag nur als Anhaltspunkt gesehen werden. Gerne auch eigene Ideen anbieten.

```html
<!DOCTYPE html>
<html lang="de">
<head>
<meta charset="utf-8">
<title>Glückskekse – Faltschachtel</title>
<link rel="stylesheet" href="https://fonts.googleapis.com/css2?family=Great+Vibes&family=Roboto+Condensed:wght@400;700&display=swap">
<style>
  :root{
    --page:#ffffff;
    --sheet:#d9d9d9;
    --carton:#faf5f2;
    --cut:#c9c4c0;
    --band-foot:#ece8e2;
    --gold:#d6b25c;
    --gold-deep:#b8913a;
    --sage:#9fb59a;
    --sage-deep:#4f6e58;
    --sage-light:#dfe8da;
    --butter:#efe1a8;
    --ink:#333333;
  }
  html,body{margin:0;padding:0;width:706px;height:1200px;overflow:hidden;background:var(--page);}
  .dieline{position:absolute;left:0;top:352px;width:706px;height:495px;display:block;}
  .sheet{fill:var(--sheet);}
  .panel{fill:var(--carton);stroke:var(--cut);stroke-width:2;}
  .fold{stroke:var(--cut);stroke-width:1.5;fill:none;}
  .band-foot{fill:var(--band-foot);}
  .wreath-ring{fill:none;stroke:var(--gold);stroke-width:2.5;}
  .greeting{font-family:"Great Vibes",cursive;fill:var(--gold);font-size:44px;text-anchor:middle;}
  .info{font-family:"Roboto Condensed",sans-serif;fill:var(--ink);font-size:10px;}
  .info-bold{font-weight:700;}
  .claim{font-family:"Roboto Condensed",sans-serif;fill:var(--ink);font-size:12px;letter-spacing:0.5px;text-anchor:middle;}
  .net{font-family:"Roboto Condensed",sans-serif;fill:var(--ink);font-size:15px;text-anchor:middle;}
  .nutri-frame{fill:none;stroke:var(--ink);stroke-width:1.2;}
  .nutri-rule{stroke:var(--ink);stroke-width:0.6;}
  .badge{fill:var(--sage-deep);}
  .dot{fill:var(--gold);}
</style>
</head>
<body>
<svg class="dieline" viewBox="0 0 1482 1040" xmlns="http://www.w3.org/2000/svg">
  <defs>
    <linearGradient id="floral-band" x1="0" y1="0" x2="1" y2="0">
      <stop offset="0" stop-color="#c9d6c2"/>
      <stop offset="0.12" stop-color="#e6ece0"/>
      <stop offset="0.3" stop-color="#e9e2b8"/>
      <stop offset="0.4" stop-color="#a9bea4"/>
      <stop offset="0.5" stop-color="#7f9c83"/>
      <stop offset="0.6" stop-color="#a9bea4"/>
      <stop offset="0.7" stop-color="#e9e2b8"/>
      <stop offset="0.88" stop-color="#e6ece0"/>
      <stop offset="1" stop-color="#c9d6c2"/>
    </linearGradient>
    <linearGradient id="floral-fade" x1="0" y1="0" x2="0" y2="1">
      <stop offset="0" stop-color="#faf5f2" stop-opacity="0.85"/>
      <stop offset="0.35" stop-color="#faf5f2" stop-opacity="0.1"/>
      <stop offset="1" stop-color="#faf5f2" stop-opacity="0.3"/>
    </linearGradient>
    <linearGradient id="branch" x1="0" y1="1" x2="1" y2="0">
      <stop offset="0" stop-color="#f3ead0"/>
      <stop offset="1" stop-color="#8fae9a"/>
    </linearGradient>
  </defs>

  <rect class="sheet" x="0" y="0" width="1482" height="1040"/>

  <!-- glue flap -->
  <path class="panel" d="M52,440 L15,458 L15,770 L52,782 Z"/>

  <!-- lid with tuck flap -->
  <path class="panel" d="M60,86 L60,62 Q60,12 112,12 L358,12 Q410,12 410,62 L410,86 Z"/>
  <rect class="panel" x="55" y="86" width="357" height="347"/>

  <!-- top dust flaps -->
  <path class="panel" d="M420,433 L420,222 L706,222 L762,418 L762,433 Z"/>
  <path class="panel" d="M1113,433 L1113,418 L1170,222 L1452,222 L1452,433 Z"/>

  <!-- bottom closures -->
  <path class="panel" d="M55,788 L55,800 L140,955 L140,1000 Q140,1025 165,1025 L300,1025 Q325,1025 325,1000 L325,955 L410,800 L410,788 Z"/>
  <path class="panel" d="M412,788 L412,1000 L583,1000 L583,880 L762,792 L762,788 Z"/>
  <path class="panel" d="M762,788 L762,1027 L850,1027 L850,952 L1028,952 L1028,1027 L1113,1027 L1113,788 Z"/>
  <path class="panel" d="M1113,788 L1113,792 L1290,880 L1290,1000 L1465,1000 L1465,788 Z"/>

  <!-- wrap band -->
  <rect class="panel" x="52" y="433" width="1418" height="355"/>
  <rect class="band-foot" x="53" y="735" width="1416" height="52"/>
  <g role="img" aria-label="Aquarell-Blütenranke mit salbeigrünen Lilien, Blättern, goldenen Linien und Punkten">
    <rect x="53" y="445" width="1416" height="300" fill="url(#floral-band)"/>
    <rect x="53" y="445" width="1416" height="300" fill="url(#floral-fade)"/>
  </g>
  <line class="fold" x1="412" y1="433" x2="412" y2="788"/>
  <line class="fold" x1="762" y1="433" x2="762" y2="788"/>
  <line class="fold" x1="1113" y1="433" x2="1113" y2="788"/>

  <!-- lid artwork -->
  <circle class="wreath-ring" cx="235" cy="282" r="140"/>
  <g role="img" aria-label="Aquarell-Zweig mit grünen Blättern und goldener Blüte">
    <path d="M190,150 Q260,95 375,150 L375,215 Q300,150 190,175 Z" fill="url(#branch)"/>
  </g>
  <circle class="dot" cx="103" cy="137" r="5"/>
  <circle class="dot" cx="372" cy="390" r="5"/>
  <circle class="dot" cx="110" cy="205" r="3"/>
  <text class="greeting" x="240" y="258">Schön,</text>
  <text class="greeting" x="240" y="306">dass du da bist!</text>

  <!-- manufacturer side -->
  <circle class="badge" cx="138" cy="855" r="15"/>
  <g transform="translate(190,822) rotate(-90)">
    <text class="info" text-anchor="end" x="0" y="0">Hergestellt für:</text>
    <text class="info" text-anchor="end" x="0" y="13">SunnyBites</text>
    <text class="info" text-anchor="end" x="0" y="26">Wiesenweg 7</text>
    <text class="info" text-anchor="end" x="0" y="39">93099 Feldkirch</text>
    <text class="info" text-anchor="end" x="0" y="77">Mindestens haltbar bis:</text>
  </g>
  <text class="claim" transform="translate(235,970) rotate(180)">VEGAN - REGIONAL - LECKER</text>

  <!-- ingredients side -->
  <g transform="translate(1058,800) rotate(90)">
    <text class="info info-bold" x="0" y="0">12 St. Glückskekse</text>
    <text class="info" x="0" y="22">Zutaten:</text>
    <text class="info" x="0" y="34"><tspan class="info-bold">Weizenmehl</tspan>, Zucker, pflanzliches Öl (Raps),</text>
    <text class="info" x="0" y="46">Aroma, Emulgator Sonnenblumenlecithin,</text>
    <text class="info" x="0" y="58">Speisesalz, Backtriebmittel Natriumcarbonat.</text>
    <text class="info" x="0" y="70">KÜHL UND TROCKEN LAGERN.</text>
    <text class="info" x="0" y="94"><tspan class="info-bold">Weizengebäck</tspan> mit einem Zettel im Inneren!</text>
    <text class="info" x="0" y="106">Hergestellt in EU • Produziert in Bayern</text>
    <text class="info" x="0" y="118">Für Kinder unter 3 Jahren nicht geeignet.</text>
    <text class="info" x="0" y="130">Vor dem Verzehr Innenzettel herausnehmen!</text>
    <text class="info" x="0" y="150">Durchschnittliche Nährwerte</text>
    <rect class="nutri-frame" x="0" y="158" width="180" height="110"/>
    <line class="nutri-rule" x1="0" y1="172" x2="180" y2="172"/>
    <text class="info" x="4" y="168">pro 100 g</text>
    <text class="info" x="4" y="184">Energie</text><text class="info" x="176" y="184" text-anchor="end">1637 kJ/387 kcal</text>
    <text class="info" x="4" y="196">Fett</text><text class="info" x="176" y="196" text-anchor="end">4,7 g</text>
    <text class="info" x="4" y="208">davon gesättigte Fettsäuren</text><text class="info" x="176" y="208" text-anchor="end">0,1 g</text>
    <text class="info" x="4" y="220">Kohlenhydrate</text><text class="info" x="176" y="220" text-anchor="end">79,5 g</text>
    <text class="info" x="4" y="232">davon Zucker</text><text class="info" x="176" y="232" text-anchor="end">39,9 g</text>
    <text class="info" x="4" y="244">Ballaststoffe</text><text class="info" x="176" y="244" text-anchor="end">2,3 g</text>
    <text class="info" x="4" y="256">Eiweiß</text><text class="info" x="176" y="256" text-anchor="end">5,5 g</text>
    <text class="info" x="4" y="266">Salz</text><text class="info" x="176" y="266" text-anchor="end">0,13 g</text>
  </g>
  <text class="net" x="938" y="980">℮ 12 x 7g</text>
</svg>
</body>
</html>
```